Vessora Goods Company (importer of Latin American foods)

We seek to be the N1 distributor in Europe with Latin American quality products, we seek a sober catalog design where white and black predominate, with a professional and luxurious appearance. We seek to use an image that characterizes us a lot about Latin American looks and to give information about the brands that we represent from Latin America, we seek to have long-term contact with the designer since it will undergo changes during the first year

Target Market(s)

Retail channel, cash and carry's and distributors

Industry/Entity Type

Supermarket

Font styles to use
Sans Serif

Requirements
Must have
• It has to be a catalog that represents Latin American cultural diversity, the brands that we export from Argentina to Mexico are premium and the catalog must be in accordance with our brands
Nice to have
• Map of Latin America, Photos of Latin America, brief description of our brands, description of our company, black and white typography. Our logo must be on each sheet of the catalog, easily modifiable format to add future brands
Should not have
• We are open to designer suggestions

```html
<!DOCTYPE html>
<html lang="en">
<head>
<meta charset="utf-8">
<title>Vessora Goods Company — Catalog Spreads</title>
<link rel="stylesheet" href="https://fonts.googleapis.com/css2?family=Open+Sans:wght@400;600;700&display=swap">
<style>
  :root {
    --backdrop: #ececec;
    --paper: #ffffff;
    --ink: #2b2b2b;
    --ink-soft: #6a6a6a;
    --headline-light: rgba(255, 255, 255, 0.82);
    --spine-shadow: rgba(0, 0, 0, 0.12);
  }
  * { box-sizing: border-box; margin: 0; padding: 0; }
  html, body {
    width: 1200px; height: 1200px; overflow: hidden;
    background: var(--backdrop);
    font-family: "Open Sans", Arial, sans-serif;
    color: var(--ink);
  }
  .canvas {
    position: relative; width: 1200px; height: 1200px;
  }
  .spread {
    position: absolute; left: 50px; width: 1100px; height: 550px;
    display: flex; background: var(--paper);
    box-shadow: 0 6px 18px rgba(0,0,0,0.08);
  }
  .spread--feature { top: 30px; }
  .spread--produce { top: 620px; }
  .page { position: relative; width: 550px; height: 550px; overflow: hidden; }
  .page--left::after {
    content: ""; position: absolute; top: 0; right: 0; width: 28px; height: 100%;
    background: linear-gradient(to left, var(--spine-shadow), transparent);
  }
  .page--right::before {
    content: ""; position: absolute; top: 0; left: 0; width: 22px; height: 100%;
    background: linear-gradient(to right, var(--spine-shadow), transparent);
    z-index: 2;
  }

  /* Feature spread — left page */
  .photo-chef {
    position: absolute; inset: 0;
    background:
      radial-gradient(ellipse at 45% 88%, #f4a13a 0%, #e0701e 18%, rgba(90,60,40,0.0) 42%),
      linear-gradient(160deg, #d9dcde 0%, #b9bec1 45%, #6f7375 78%, #3a3a3a 100%);
  }
  .headline-tag {
    position: absolute; left: 36px; top: 190px;
    font-size: 46px; font-weight: 600; letter-spacing: 2px;
    white-space: nowrap;
    color: var(--headline-light);
  }
  .photo-caption {
    position: absolute; left: 36px; bottom: 70px; width: 280px;
    font-size: 10px; line-height: 1.55; color: rgba(255,255,255,0.85);
  }

  /* Feature spread — right page */
  .profile {
    position: absolute; right: 46px; top: 44px; width: 110px; text-align: center;
  }
  .profile__photo {
    width: 96px; height: 96px; border-radius: 50%; margin: 0 auto 10px;
    background: linear-gradient(135deg, #c9a38d, #7d5a4b);
  }
  .profile__name { font-size: 11px; font-weight: 700; }
  .profile__role { font-size: 8px; color: var(--ink-soft); }
  .body-columns {
    position: absolute; left: 56px; right: 46px; top: 250px;
    display: grid; grid-template-columns: 1fr 1fr; column-gap: 26px;
  }
  .body-columns p {
    font-size: 10.5px; line-height: 1.6; color: var(--ink-soft); margin-bottom: 12px;
  }

  /* Produce spread */
  .photo-corn {
    position: absolute; inset: 0; width: 1100px; height: 550px;
    background:
      radial-gradient(ellipse at 20% 30%, #5a2a2e 0%, transparent 40%),
      radial-gradient(ellipse at 45% 60%, #d0582a 0%, transparent 38%),
      radial-gradient(ellipse at 62% 35%, #efe6cf 0%, transparent 30%),
      radial-gradient(ellipse at 70% 82%, #f0c24a 0%, transparent 32%),
      radial-gradient(ellipse at 88% 40%, #d9708a 0%, transparent 34%),
      linear-gradient(120deg, #7a3a2c, #b64a3c 40%, #c25a6c 70%, #3b6a8a);
  }
  .spread--produce .page { position: relative; z-index: 1; background: transparent; }
  .site-address {
    position: absolute; right: 54px; top: 240px; z-index: 3;
    font-size: 34px; font-weight: 600; color: #ffffff; white-space: nowrap;
  }
</style>
</head>
<body>
<main class="canvas">

  <section class="spread spread--feature">
    <article class="page page--left">
      <div class="photo-chef" role="img" aria-label="Photo of a chef in white jacket flambéing a pan over high flames in a professional kitchen"></div>
      <h1 class="headline-tag">#WEARELATINOS</h1>
      <p class="photo-caption">Our kitchens carry recipes from many lands, shared at every table across the region, prepared with care, patience and the finest harvest of each season.</p>
    </article>
    <article class="page page--right">
      <div class="profile">
        <div class="profile__photo" role="img" aria-label="Round portrait photo of a smiling woman"></div>
        <p class="profile__name">Name name</p>
        <p class="profile__role">Chef</p>
      </div>
      <div class="body-columns">
        <div>
          <p>We bring premium products from Argentina to Mexico to shelves across Europe, selected with producers who share our respect for origin and quality.</p>
          <p>Each brand tells a story of land, family and craft, carried with care from field to table and presented with clarity for every partner.</p>
          <p>Retail chains, cash and carry stores and distributors find a trusted source in one place.</p>
        </div>
        <div>
          <p>Our range grows each season as new producers join us, keeping flavour, tradition and consistent supply at the heart of every order we send.</p>
          <p>From corn and grains to sauces and sweets, every product is chosen to represent the diversity of the region.</p>
          <p>Talk with our team to learn more.</p>
        </div>
      </div>
    </article>
  </section>

  <section class="spread spread--produce">
    <div class="photo-corn" role="img" aria-label="Full-spread photo of colourful Andean corn cobs in purple, red, orange, white and yellow on a woven textile"></div>
    <article class="page page--left"></article>
    <article class="page page--right">
      <p class="site-address">vessoragoodscompany.com</p>
    </article>
  </section>

</main>
</body>
</html>
```